Print and E-book Personal Injury Front and Back Book Cover

I need a book cover for a personal injury law firm book titled "Rising Past the Wreckage" with the subtitle "A Plain Guide for Harmed Readers." The book cover should have an image. This isas a lead generation book designed to be give to potential clients to have them sign as new clients.

Target Market(s)

Potential New Clients Looking For a Personal Injury Attorney

Industry/Entity Type

Legal

Requirements
Must have
• Title and some type of image or images

```html
<!DOCTYPE html>
<html lang="en">
<head>
<meta charset="utf-8">
<title>Rising Past the Wreckage – Book Cover</title>
<link href="https://fonts.googleapis.com/css2?family=Lora:wght@400;500&family=Montserrat:wght@800&display=swap" rel="stylesheet">
<style>
  :root {
    --stage: #c9d0d1;
    --paper-top: #f1f4f7;
    --paper-bottom: #ffffff;
    --ink: #262626;
    --accent: #d98a0b;
    --tag-text: #e9eef2;
    --photo-light: #e9eef3;
    --photo-mid: #b4c1ce;
    --photo-dark: #4a3f39;
  }
  * { margin: 0; padding: 0; box-sizing: border-box; }
  html, body {
    width: 1066px;
    height: 1200px;
    overflow: hidden;
    background: var(--stage);
  }
  .cover {
    position: absolute;
    left: 167px;
    top: 50px;
    width: 732px;
    height: 1100px;
    background: linear-gradient(180deg, var(--paper-top) 0%, var(--paper-bottom) 45%, var(--paper-top) 100%);
    overflow: hidden;
  }
  .title {
    position: absolute;
    left: 0;
    top: 95px;
    width: 100%;
    text-align: center;
    color: var(--ink);
  }
  .title-lead {
    display: block;
    font-family: "Lora", serif;
    font-weight: 400;
    font-size: 62px;
    line-height: 1;
  }
  .title-main {
    display: block;
    font-family: "Montserrat", sans-serif;
    font-weight: 800;
    font-size: 156px;
    line-height: 0.86;
    letter-spacing: -4px;
    margin-top: 2px;
  }
  .title-link {
    position: relative;
    z-index: 2;
    display: inline-block;
    background: var(--ink);
    color: var(--tag-text);
    font-family: "Lora", serif;
    font-size: 52px;
    line-height: 46px;
    padding: 0 48px 4px;
    margin-top: -10px;
    transform: rotate(-2deg);
  }
  .title-accent {
    display: block;
    font-family: "Montserrat", sans-serif;
    font-weight: 800;
    font-size: 96px;
    line-height: 0.92;
    letter-spacing: -2px;
    color: var(--accent);
    margin-top: -10px;
  }
  .subtitle {
    position: absolute;
    left: 0;
    top: 468px;
    width: 100%;
    text-align: center;
    font-family: "Lora", serif;
    font-size: 28px;
    color: var(--ink);
  }
  .cover-photo {
    position: absolute;
    left: 60px;
    top: 535px;
    width: 612px;
    height: 420px;
    border-radius: 6px;
    background: linear-gradient(165deg, var(--photo-light) 0%, var(--photo-mid) 50%, var(--photo-dark) 100%);
  }
  .author {
    position: absolute;
    left: 0;
    top: 990px;
    width: 100%;
    text-align: center;
    font-family: "Lora", serif;
    font-size: 52px;
    color: var(--ink);
  }
</style>
</head>
<body>
  <main class="cover">
    <h1 class="title">
      <span class="title-lead">Rising</span>
      <span class="title-main">PAST</span>
      <span class="title-link">the</span>
      <span class="title-accent">WRECKAGE</span>
    </h1>
    <p class="subtitle">A Plain Guide for Harmed Readers</p>
    <div class="cover-photo" role="img" aria-label="Photo of a wooden judge's gavel on its block beside a stethoscope on a white surface"></div>
    <p class="author">Author Name</p>
  </main>
</body>
</html>
```